Thank You Card for Customer Purchase

I need a thank you card designed to go out with my product once a customer has purchased. It will require some content creation but only a couple of lines.

It needs be basically state something along the lines of

"Thank you for your purchase..........
as well as some sort of speal about the company as well as contact details"

I have attached our brand guide to assist you. I will also provide you the url so you may get an idea of the company and the way we talk.

The document should be double sided A5 In size Landscape and be print ready as well. Provided in illustrator and pdf files. I have attached a template that is to be used and there is a printing instructions PDF document you need to follow as well.

Please contact if you have any questions

Target Market(s)

Young people aroung 20-40 male and female. Cool people

Industry/Entity Type

Printing

Requirements
Must have
• be cool and inline with brand guideline. please check out www.brodymarsh.com.au for ideas.

```html
<!DOCTYPE html>
<html lang="en">
<head>
<meta charset="utf-8">
<title>Brody Marsh — Thank You Card</title>
<link rel="stylesheet" href="https://fonts.googleapis.com/css2?family=Exo+2:wght@300;400&family=Kalam:wght@300&display=swap">
<style>
  :root {
    --page-bg: #a87c52;
    --card-white: #ffffff;
    --ink-grey: #4a4a4a;
    --accent-blue: #3d6fb8;
    --accent-orange: #f07a3c;
    --art-light: #c9c5c3;
    --art-dark: #55575a;
    --back-dark: #2a2a2a;
    --back-darker: #161616;
    --back-text: #f2f2f2;
  }
  html, body {
    margin: 0;
    padding: 0;
    width: 867px;
    height: 1200px;
    overflow: hidden;
    background: var(--page-bg);
    font-family: "Exo 2", sans-serif;
  }
  .card {
    position: absolute;
    overflow: hidden;
  }
  .card--front {
    left: 103px;
    top: 91px;
    width: 701px;
    height: 495px;
    background: var(--card-white);
  }
  .card--back {
    left: 91px;
    top: 614px;
    width: 703px;
    height: 493px;
  }
  .front__art {
    position: absolute;
    left: 0;
    top: 0;
    width: 298px;
    height: 495px;
    background: linear-gradient(160deg, var(--art-light) 0%, #a9a8a8 35%, var(--art-dark) 70%, #d4d4d4 100%);
  }
  .front__brand {
    position: absolute;
    right: 30px;
    top: 110px;
    margin: 0;
    font-weight: 300;
    font-size: 15px;
    line-height: 18px;
    letter-spacing: 3px;
    color: var(--ink-grey);
  }
  .front__product {
    position: absolute;
    left: 384px;
    top: 292px;
    width: 233px;
    height: 80px;
    background: linear-gradient(120deg, #7a1f1f 0%, #c84a2a 50%, var(--accent-orange) 100%);
    border-radius: 6px;
  }
  .front__thanks {
    position: absolute;
    right: 30px;
    top: 386px;
    margin: 0;
    text-align: right;
    font-weight: 400;
    font-size: 24px;
    line-height: 25px;
    letter-spacing: 0.5px;
    color: var(--accent-blue);
  }
  .front__rule {
    position: absolute;
    right: 30px;
    top: 443px;
    width: 252px;
    height: 1px;
    background: var(--accent-orange);
  }
  .front__contact {
    position: absolute;
    right: 30px;
    top: 449px;
    margin: 0;
    font-family: "Kalam", cursive;
    font-weight: 300;
    font-size: 12px;
    line-height: 16px;
    color: var(--ink-grey);
    white-space: nowrap;
  }
  .front__contact span + span { margin-left: 14px; }
  .back__texture {
    position: absolute;
    inset: 0;
    background: linear-gradient(180deg, var(--back-dark) 0%, #3a3a3a 30%, var(--back-darker) 55%, #333 80%, var(--back-darker) 100%);
  }
  .back__brand {
    position: absolute;
    left: 0;
    right: 0;
    top: 280px;
    margin: 0;
    text-align: center;
    font-weight: 300;
    font-size: 19px;
    line-height: 22px;
    letter-spacing: 4px;
    color: var(--back-text);
  }
</style>
</head>
<body>
  <section class="card card--front">
    <div class="front__art" role="img" aria-label="Abstract grey paint splash artwork with tall dark peak shape"></div>
    <h1 class="front__brand">BRODY MARSH</h1>
    <div class="front__product" role="img" aria-label="Photo of red and orange rectangular eyeglasses"></div>
    <p class="front__thanks">THANK YOU<br>FOR YOUR PURCHASE</p>
    <div class="front__rule"></div>
    <p class="front__contact"><span>Call us 1300 555 204</span><span>www.brodymarsh.com.au</span></p>
  </section>

  <section class="card card--back">
    <div class="back__texture" role="img" aria-label="Dark brushed metal texture background"></div>
    <h2 class="back__brand">BRODY MARSH</h2>
  </section>
</body>
</html>
```